QBoost480 Business Card Design

I am in need of a business card design.

Business Name: Quantum Boost 480 or Qboost480 (we can try the business card with both variations)

I would like it to be somewhat different from the "average" business card

What do we do?

We link up with distributors of different items and we Market their products, sell their products, fulfill the shipment, and handle all customer service that goes along with it.

I will be uploading our logo as well as other business card ideas that i have seen and liked on the web.

I like the style of the "graphic design" business card that i uploaded. I was thinking maybe something like that but instead would read.

SYNC | SELL | SHIP

With maybe:
a computer or a Sync icon underneath SYNC
Some form of money sign underneath Sell
a delivery truck or something underneath SHIP.

And then I was thinking maybe put the logo on the back side like in the other business card that i uploaded.

I definitely want a double sided business card.

These are only my suggestions and if i was very confident in my idea then I wouldn't have to be on here. (So make what you think is nice because my opinion is probably not so great anyway!!)

Everything can be changed.

ALSO, For the logo
We can try and remove the text multi channel selling

For the Business card contact info:
Milo Quenton
CEO
2914 Ravensby Street
J7T-2K8
Montreal, Quebec

Thanks

Target Market(s)

Businesses

Industry/Entity Type

Information Technology

Font styles to use
Serif
Sans Serif
Decorative

Colors
34a6d6
33b8a4
aaaaaa
85cae6
33a6d7
0492cd
9d9d9d

Requirements
Must have
• Double Sided Business card
Nice to have
• Illustration graphics / Icons underneath the main points

```html
<!DOCTYPE html>
<html lang="en">
<head>
<meta charset="utf-8">
<title>QBoost480 Business Card</title>
<link rel="stylesheet" href="https://fonts.googleapis.com/css2?family=Bebas+Neue&family=Open+Sans:ital,wght@0,300;0,400;1,400&display=swap">
<style>
  :root {
    --backdrop: #8de8ea;
    --card: #ffffff;
    --band-end: #a9f0f2;
    --brand-cyan: #1fe0f0;
    --brand-blue: #3ab1ef;
    --ink: #111111;
    --tag-grey: #6f8183;
    --icon-grey: #6b6b6b;
  }
  * { margin: 0; padding: 0; box-sizing: border-box; }
  html, body { width: 1200px; height: 1200px; overflow: hidden; }
  body { background: var(--backdrop); position: relative; font-family: "Open Sans", sans-serif; }

  .card {
    position: absolute;
    background: var(--card);
    border-radius: 34px;
    overflow: hidden;
    box-shadow: 6px 8px 10px rgba(40, 110, 115, 0.45);
  }
  .card-front { left: 166px; top: 62px; width: 868px; height: 509px; }
  .card-back  { left: 162px; top: 630px; width: 868px; height: 509px; }

  .front-band {
    position: absolute; left: 0; right: 0; top: 312px; bottom: 0;
    background: linear-gradient(90deg, #ffffff 0%, #e6fbfb 25%, #c4f4f5 60%, var(--band-end) 100%);
  }
  .front-wordmark {
    position: absolute; left: 82px; top: 168px;
    font-family: "Bebas Neue", sans-serif; font-size: 96px; line-height: 1;
    color: var(--brand-cyan); letter-spacing: 1px;
  }
  .front-wordmark-dot {
    position: absolute; left: 420px; top: 150px; width: 30px; height: 30px;
    border-radius: 50%; background: var(--brand-cyan);
  }
  .holder { position: absolute; right: 90px; top: 216px; text-align: right; }
  .holder-name {
    font-family: "Bebas Neue", sans-serif; font-size: 56px; line-height: 1;
    color: var(--ink); letter-spacing: 0.5px;
  }
  .holder-title {
    font-style: italic; font-size: 22px; line-height: 1; margin-top: 6px; color: var(--ink);
  }
  .address {
    position: absolute; left: 576px; top: 348px;
    font-family: "Bebas Neue", sans-serif; font-size: 27px; line-height: 32px;
    color: var(--ink); letter-spacing: 1px;
  }

  .back-wordmark {
    position: absolute; left: 0; right: 0; top: 148px; text-align: center;
    font-weight: 300; font-size: 104px; line-height: 1; color: var(--brand-blue);
    letter-spacing: 2px;
  }
  .services { position: absolute; left: 0; top: 288px; width: 868px; height: 120px; }
  .service-label {
    position: absolute; top: 0; transform: translateX(-50%);
    font-size: 32px; line-height: 40px; color: var(--tag-grey);
  }
  .service-divider {
    position: absolute; top: 6px; width: 2px; height: 32px; background: var(--tag-grey);
  }
  .service-icon { position: absolute; top: 56px; width: 52px; height: 52px; transform: translateX(-50%); }
</style>
</head>
<body>
  <section class="card card-front">
    <div class="front-band"></div>
    <div class="front-wordmark">Qboost480</div>
    <div class="front-wordmark-dot"></div>
    <div class="holder">
      <div class="holder-name">MILO QUENTON</div>
      <div class="holder-title">CEO</div>
    </div>
    <div class="address">
      2914 RAVENSBY STREET<br>
      J7T-2K8, MONTREAL<br>
      QUEBEC
    </div>
  </section>

  <section class="card card-back">
    <div class="back-wordmark">QBoost480</div>
    <div class="services">
      <span class="service-label" style="left:320px">SYNC</span>
      <span class="service-divider" style="left:382px"></span>
      <span class="service-label" style="left:440px">SELL</span>
      <span class="service-divider" style="left:497px"></span>
      <span class="service-label" style="left:555px">SHIP</span>

      <svg class="service-icon" style="left:322px" viewBox="0 0 52 52" aria-label="Sync">
        <circle cx="26" cy="26" r="26" fill="var(--icon-grey)"/>
        <path d="M13 24 A13 13 0 0 1 37 19" fill="none" stroke="#fff" stroke-width="4"/>
        <polygon points="33,13 42,17 36,25" fill="#fff"/>
        <path d="M39 28 A13 13 0 0 1 15 33" fill="none" stroke="#fff" stroke-width="4"/>
        <polygon points="19,39 10,35 16,27" fill="#fff"/>
      </svg>
      <svg class="service-icon" style="left:435px" viewBox="0 0 52 52" aria-label="Sell">
        <circle cx="26" cy="26" r="26" fill="var(--icon-grey)"/>
        <text x="26" y="37" text-anchor="middle" font-family="Open Sans, sans-serif" font-weight="700" font-size="32" fill="#fff">$</text>
      </svg>
      <svg class="service-icon" style="left:548px" viewBox="0 0 52 52" aria-label="Ship">
        <circle cx="26" cy="26" r="26" fill="var(--icon-grey)"/>
        <path d="M10 17 H34 L42 26 V34 H10 Z" fill="#fff"/>
        <path d="M34 19 L40 26 H34 Z" fill="var(--icon-grey)"/>
        <rect x="6" y="20" width="12" height="2" fill="var(--icon-grey)"/>
        <rect x="6" y="24" width="10" height="2" fill="var(--icon-grey)"/>
        <rect x="6" y="28" width="12" height="2" fill="var(--icon-grey)"/>
        <circle cx="18" cy="35" r="4" fill="var(--icon-grey)" stroke="#fff" stroke-width="2"/>
        <circle cx="35" cy="35" r="4" fill="var(--icon-grey)" stroke="#fff" stroke-width="2"/>
      </svg>
    </div>
  </section>
</body>
</html>
```